law firm business cards

I need a business card using my existing logo. Two sided is best because there is a lot of information that needs to go on the card. Use the same general color scheme as logo, but I need one set with the blue background of my website (www.halvorsenlawgrp.com), and one set with white background (to see which one I like best).

Information that must be on there:
Trevor J. Halvorsen
Board Certified Civil Trial Specialist
738 Brinkley Ave., Suite 640
Raleigh, NC 27601

T 919-555-0143
F 919-555-0176

www.halvorsenlawgrp.com
trevor@halvorsenlawgrp.com

Personal Injury | Criminal Law (to separate the two, pls use a bullet point or pipeline symbol "|"

If there is a way to work in the CPRS logo (maybe at the bottom somewhere), put it in, but don't let it detract from the main logo too much.

Also, if there is a way to work it in, put in somewhere: Former Insurance Company Attorney | Former Criminal Prosecutor (to separate the two, pls use a bullet point or pipeline symbol "|"

```html
<!DOCTYPE html>
<html lang="en">
<head>
<meta charset="utf-8">
<title>Halvorsen Law – Business Cards</title>
<link rel="stylesheet" href="https://fonts.googleapis.com/css2?family=Tinos:wght@400;700&display=swap">
<style>
  :root {
    --stage: #e4e2de;
    --navy: #1f3a6e;
    --navy-deep: #18305c;
    --sky: #a9c3e6;
    --ink: #1b1b1b;
    --paper: #ffffff;
    --silver: #c9ced6;
  }
  * { box-sizing: border-box; margin: 0; padding: 0; }
  html, body { width: 1200px; height: 803px; overflow: hidden; }
  body {
    background: var(--stage);
    font-family: "Tinos", "Times New Roman", serif;
    position: relative;
  }
  .card {
    position: absolute;
    top: 253px;
    width: 520px;
    height: 297px;
    box-shadow: 0 6px 18px rgba(0,0,0,.18);
  }
  .card--front { left: 50px; background: linear-gradient(160deg, var(--navy) 0%, var(--navy-deep) 100%); }
  .card--back  { left: 630px; background: var(--paper); }

  /* front */
  .front-mark {
    position: absolute; left: 0; right: 0; top: 112px;
    display: flex; justify-content: center; align-items: center; gap: 14px;
  }
  .mark-dot {
    width: 36px; height: 36px; border-radius: 50%;
    background: var(--silver); flex: none;
  }
  .front-name {
    font-size: 42px; font-weight: 400; color: #ffffff; line-height: 1;
  }
  .front-tagline {
    position: absolute; left: 0; right: 0; top: 180px; text-align: center;
    font-size: 13px; letter-spacing: 2px; text-transform: uppercase; color: var(--sky);
  }

  /* back */
  .back-mark {
    position: absolute; left: 26px; top: 36px;
    display: flex; align-items: center; gap: 8px;
  }
  .back-mark .mark-dot { width: 20px; height: 20px; background: var(--navy); }
  .back-name { font-size: 24px; font-weight: 400; color: var(--navy); line-height: 1; }
  .badge {
    position: absolute; right: 22px; top: 20px;
    width: 36px; height: 36px; border-radius: 50%;
    border: 2px solid var(--navy); background: #eef1f7;
  }
  .person { position: absolute; left: 150px; top: 112px; }
  .person-name { font-size: 24px; letter-spacing: 1px; color: var(--ink); text-transform: uppercase; }
  .person-title { font-size: 14px; color: var(--ink); margin-top: 3px; }

  .contact { position: absolute; list-style: none; font-size: 14px; color: var(--ink); }
  .contact li { display: flex; align-items: center; gap: 8px; line-height: 21px; white-space: nowrap; }
  .contact svg { width: 12px; height: 12px; fill: var(--ink); flex: none; }
  .contact--phones { left: 36px; top: 204px; }
  .contact--details { left: 300px; top: 196px; }
  .contact .indent { padding-left: 20px; }
</style>
</head>
<body>

<section class="card card--front" aria-label="Front of card">
  <div class="front-mark">
    <span class="mark-dot" aria-hidden="true"></span>
    <span class="front-name">Halvorsen Law</span>
  </div>
  <p class="front-tagline">Personal Injury | Criminal Law</p>
</section>

<section class="card card--back" aria-label="Back of card">
  <div class="back-mark">
    <span class="mark-dot" aria-hidden="true"></span>
    <span class="back-name">Halvorsen Law</span>
  </div>
  <span class="badge" role="img" aria-label="Certification badge"></span>

  <div class="person">
    <p class="person-name">Trevor J. Halvorsen</p>
    <p class="person-title">Board Certified Civil Trial Specialist</p>
  </div>

  <ul class="contact contact--phones">
    <li><svg viewBox="0 0 12 12"><path d="M2 1h3l1 3-2 1a7 7 0 0 0 3 3l1-2 3 1v3c-6 0-10-4-10-9z"/></svg>919.555.0143</li>
    <li><svg viewBox="0 0 12 12"><path d="M3 0h6v12H3zM4 1v9h4V1z"/></svg>919.555.0158</li>
    <li><svg viewBox="0 0 12 12"><path d="M1 4h10v6H1zM3 0h6v3H3z"/></svg>919.555.0176</li>
  </ul>

  <ul class="contact contact--details">
    <li><svg viewBox="0 0 12 12"><path d="M0 2h12v8H0zM1 3l5 4 5-4z" fill-rule="evenodd"/></svg>trevor@halvorsenlawgrp.com</li>
    <li><svg viewBox="0 0 12 12"><circle cx="6" cy="6" r="5.5"/></svg>www.halvorsenlawgrp.com</li>
    <li><svg viewBox="0 0 12 12"><path d="M6 0a4 4 0 0 1 4 4c0 3-4 8-4 8S2 7 2 4a4 4 0 0 1 4-4z"/></svg>738 Brinkley Ave., Suite 640</li>
    <li class="indent">Raleigh, NC 27601</li>
  </ul>
</section>

</body>
</html>
```